Willowmere Spa and Beauty Ltd. (Name of business)

I need a business card designed for this new company based out of Toronto Ontario. We specialize in Eyelash Extensions, Manicures and Pedicures, body waxing, massages, laser hair removal and botox treatments. Also offer a variety of products for sale, such as skin cream serums, collagen gel, eye cream, etc. It is a safe relaxing and non-judgemental environnment. Clients are welcome to come be pampered for the half or full day. Many service packages to choose from.

Open 7days per week from 8am to 8pm.

Priscilla Dunmore
Spa Facilitator
Willowmere Spa and Beauty Ltd.
7200 Harcourt St; Suite 1400
Toronto ON K2P 9W4

OFFICE: 416.790.4100
FAX: 416.790.4101
CELL: 416.632.1987
EMAIL: priscilla.dunmore@willowmerespa.com

Target Market(s)

Target market is primarily female ranging from 16 years old to 50 years old.

Industry/Entity Type

Business

Contact Information for Business Card

Priscilla Dunmore
Spa Facilitator
7200 Harcourt St; Suite 1400
Toronto ON K2P 9W4

OFFICE: 416.790.4100
FAX: 416.790.4101
CELL: 416.632.1987

Logo Text

I dont have a logo yet. I would like it simple but sophisticated and modern.

Font styles to use
Serif

Requirements
Must have
• all pertinent details such as company name, logo, name and contact information, services that are offered, including package rates
Nice to have
• Company name and logo prominent. A card that is neat and the information such as address, phone number, fax, email, etc is not too crowded but laid out in an easy to read format.
• Possibly on the back of card - some of the services offered could be listed, as well as professional cream lotions and serums. Hours of operation etc.

```html
<!DOCTYPE html>
<html lang="en">
<head>
<meta charset="utf-8">
<title>Willowmere Spa and Beauty Ltd. — Business Card</title>
<link rel="stylesheet" href="https://fonts.googleapis.com/css2?family=Open+Sans:wght@400;600&display=swap">
<style>
  :root {
    --spa-green: #3f9b2a;
    --card-white: #ffffff;
    --backdrop: #ecebe8;
    --text-light: #ffffff;
  }
  * { margin: 0; padding: 0; box-sizing: border-box; }
  html, body {
    width: 1200px;
    height: 900px;
    overflow: hidden;
    background: var(--backdrop);
    font-family: "Open Sans", Arial, sans-serif;
  }
  .canvas { position: relative; width: 1200px; height: 900px; }

  .card {
    position: absolute;
    width: 556px;
    height: 344px;
    overflow: hidden;
    box-shadow: 0 6px 18px rgba(0,0,0,0.12);
  }

  /* Front */
  .card-front {
    left: 238px;
    top: 62px;
    background: var(--spa-green);
    color: var(--text-light);
  }
  .holder-name {
    position: absolute; left: 30px; top: 26px;
    font-size: 18px; font-weight: 600; line-height: 1.2;
  }
  .holder-title {
    position: absolute; left: 30px; top: 50px;
    font-size: 14px; line-height: 1.2;
  }
  .company-block {
    position: absolute; left: 30px; top: 96px;
    font-size: 14.5px; line-height: 20px;
    font-style: normal;
  }
  .company-name { font-weight: 600; }
  .contact-list {
    position: absolute; left: 30px; top: 176px;
    list-style: none;
    font-size: 14.5px; line-height: 20px;
  }
  .contact-list li { display: flex; align-items: center; gap: 8px; }
  .contact-list .contact-email { font-size: 13.5px; letter-spacing: -0.2px; }
  .contact-list svg { width: 12px; height: 12px; fill: var(--text-light); flex: none; }
  .opening-hours {
    position: absolute; left: 28px; top: 276px;
    font-size: 14.5px; line-height: 20px;
  }
  .brand-disc {
    position: absolute; left: 304px; top: 14px;
    width: 320px; height: 320px;
    border-radius: 50%;
    background: var(--card-white);
  }
  .brand-disc-name {
    position: absolute; left: 330px; top: 160px;
    font-size: 26px; font-weight: 400; color: var(--spa-green);
    letter-spacing: 1px;
  }

  /* Back */
  .card-back {
    left: 457px;
    top: 518px;
    width: 560px;
    background: var(--card-white);
    color: var(--spa-green);
    text-align: center;
  }
  .brand-dot {
    position: absolute; left: 250px; top: 92px;
    width: 60px; height: 60px;
    border-radius: 50%;
    background: var(--spa-green);
  }
  .brand-wordmark {
    position: absolute; left: 0; right: 0; top: 172px;
    font-weight: 400; color: var(--spa-green);
  }
  .brand-wordmark .line-main { display: block; font-size: 44px; line-height: 52px; letter-spacing: 1px; }
  .brand-wordmark .line-sub { display: block; font-size: 17px; line-height: 24px; letter-spacing: 3px; }
</style>
</head>
<body>
<main class="canvas">

  <section class="card card-front" aria-label="Business card front">
    <div class="brand-disc"></div>
    <span class="brand-disc-name">Willowmere</span>

    <h1 class="holder-name">Priscilla Dunmore</h1>
    <p class="holder-title">Spa Facilitator</p>

    <address class="company-block">
      <span class="company-name">Willowmere Spa and Beauty Ltd.</span><br>
      7200 Harcourt St; Suite 1400<br>
      Toronto ON K2P 9W4
    </address>

    <ul class="contact-list">
      <li>
        <svg viewBox="0 0 24 24" aria-label="Office"><path d="M6.6 10.8a15.1 15.1 0 0 0 6.6 6.6l2.2-2.2a1 1 0 0 1 1-.25 11.4 11.4 0 0 0 3.6.57 1 1 0 0 1 1 1V20a1 1 0 0 1-1 1A17 17 0 0 1 3 4a1 1 0 0 1 1-1h3.5a1 1 0 0 1 1 1c0 1.25.2 2.45.57 3.57a1 1 0 0 1-.25 1z"/></svg>
        416.790.4100
      </li>
      <li>
        <svg viewBox="0 0 24 24" aria-label="Fax"><path d="M7 2h10v5H7z M4 8h16a2 2 0 0 1 2 2v10H2V10a2 2 0 0 1 2-2zm3 5v2h4v-2zm6 0v2h4v-2zm-6 3v2h4v-2zm6 0v2h4v-2z"/></svg>
        416.790.4101
      </li>
      <li>
        <svg viewBox="0 0 24 24" aria-label="Cell"><path d="M7 1h10a2 2 0 0 1 2 2v18a2 2 0 0 1-2 2H7a2 2 0 0 1-2-2V3a2 2 0 0 1 2-2zm0 3v14h10V4zm5 15.5a1 1 0 1 0 0 2 1 1 0 0 0 0-2z"/></svg>
        416.632.1987
      </li>
      <li class="contact-email">
        <svg viewBox="0 0 24 24" aria-label="Email"><path d="M2 5h20v14H2zm2 2v.5l8 5 8-5V7l-8 5z"/></svg>
        priscilla.dunmore@willowmerespa.com
      </li>
    </ul>

    <p class="opening-hours">Open 7days per week from<br>8am to 8pm.</p>
  </section>

  <section class="card card-back" aria-label="Business card back">
    <div class="brand-dot"></div>
    <p class="brand-wordmark">
      <span class="line-main">WILLOWMERE</span>
      <span class="line-sub">SPA AND BEAUTY LTD</span>
    </p>
  </section>

</main>
</body>
</html>
```